Football and Sports Management Agency Stationary

We have a logo, fonts, website and colour palette.
We need the logo refined by a proper designer and then business stationary designed. You can see on the website how it needs adjusting by a designers eye.
The company is a high end sports management company aiming to attract and represent professional athletes. The name Velorin is to indicate a 'Constellation of Stars' ie our clients. The dots on the star should be slightly different sizes to reflect that some clients will be bigger than others.
Colours:
#e6e6e6
#edd2a4
#caaa72 (main gold and also used on site)
#3f3f42
#001d38
#edeced (on website)
#191c23 (on website)
Font:
QT (velorin)
QT Melbrook (sports management)
We would like:
- Letterhead (word and indesign and PDF print format). I have attached an example for one I like. It's quiet a clean design with the contact details and address taking up only a small amount of room.
- Business card (dark on the back with the logo, personal details on the front). Only needs name, title, email, website and phone number. No company address (in PDF and indesign format)
- Powerpoint slide theme
- Logo in vector format for light and dark versions and single colour versions. And optimised web version
- Simple brand guide PDF showing colour, font and logo (a one/two page PDF)
Any questions, please ask.
NEW INFO:
Contact Details
Maren Solwick
Director
Mobile: +44 7630 218 977
Phone: +44 0113 872 604
Email: maren@velorinathletic.example
Web: velorinathletic.example
Corran Lodge, 14 Mill Bank Road, Stockport, SK4 9TW
Company number 40718362
Target Market(s)
Professional athletes, professional sports teams.
Industry/Entity Type
Management
Requirements
Must have
- NEW
- The designs must look cool, classy and high quality. My suggestion for this is to keep the text small and precise with uncomplicated design.
Nice to have
- Application of brand displayed on stationary and additional pieces of stationary branded.
- Draw some inspiration from the website. eg the slant angles used separate the sections.
Should not have
- Don't create new logos etc.

```html
<!DOCTYPE html>
<html lang="en">
<head>
<meta charset="utf-8">
<title>Velorin Sports Management – Letterhead</title>
<link rel="stylesheet" href="https://fonts.googleapis.com/css2?family=Open+Sans:wght@300;400;700&display=swap">
<style>
  :root {
    --backdrop: #e6e6e6;
    --paper: #ffffff;
    --gold: #caaa72;
    --ink: #191c23;
    --ink-soft: #3f3f42;
  }
  html, body {
    margin: 0;
    width: 1200px;
    height: 1000px;
    overflow: hidden;
    background: var(--backdrop);
    font-family: "Open Sans", Arial, sans-serif;
    color: var(--ink);
  }
  .letterhead {
    position: absolute;
    left: 339px;
    top: 134px;
    width: 522px;
    height: 732px;
    background: var(--paper);
    box-shadow: 0 1px 4px rgba(0,0,0,0.08);
  }
  .brand {
    position: absolute;
    left: 46px;
    top: 52px;
    display: flex;
    align-items: center;
    gap: 12px;
  }
  .brand-dot {
    width: 14px;
    height: 14px;
    border-radius: 50%;
    background: var(--gold);
  }
  .brand-name {
    font-weight: 300;
    font-size: 21px;
    letter-spacing: 6px;
    color: var(--ink-soft);
    line-height: 1;
  }
  .brand-tagline {
    position: absolute;
    left: 106px;
    top: 78px;
    font-size: 5.5px;
    letter-spacing: 2.2px;
    color: var(--ink-soft);
    font-weight: 400;
  }
  .letter {
    position: absolute;
    left: 70px;
    top: 157px;
    width: 382px;
    font-size: 8.6px;
    line-height: 11.9px;
  }
  .letter-title {
    font-weight: 700;
    font-size: 10px;
    line-height: 12px;
    margin: 0;
  }
  .letter-date { margin: 0 0 44px; }
  .salutation { margin: 0 0 7px; }
  .letter p.body {
    margin: 0 0 11px;
    text-align: justify;
  }
  .signature {
    position: absolute;
    left: 396px;
    top: 528px;
    font-size: 8.6px;
  }
  .signature-mark {
    position: absolute;
    left: 373px;
    top: 550px;
    width: 78px;
    height: 16px;
    background: linear-gradient(90deg, rgba(25,28,35,0) 0%, rgba(25,28,35,0.35) 30%, rgba(25,28,35,0.35) 70%, rgba(25,28,35,0) 100%);
    border-radius: 8px;
  }
  .contact {
    position: absolute;
    left: 31px;
    top: 655px;
    font-size: 7.6px;
    line-height: 12px;
    margin: 0;
    padding: 0;
    list-style: none;
  }
  .contact b { font-weight: 700; }
</style>
</head>
<body>
  <article class="letterhead">
    <header>
      <div class="brand">
        <span class="brand-dot"></span>
        <span class="brand-name">VELORIN</span>
      </div>
      <div class="brand-tagline">SPORTS MANAGEMENT</div>
    </header>

    <section class="letter">
      <p class="letter-title">NOTIFICATION</p>
      <p class="letter-date">2018 May 6</p>
      <p class="salutation">Dear Mr. Dallow</p>
      <p class="body">Lorem Ipsum is simply dummy text of the printing and typesetting industry. Lorem Ipsum has been the industry's standard dummy text ever since the 1500s, when an unknown printer took a galley of type and scrambled it to make a type specimen book.</p>
      <p class="body">It has survived not only five centuries, but also the leap into electronic typesetting, remaining essentially unchanged. It was popularised in the 1960s with the release of Transfera sheets containing Lorem Ipsum passages, and more recently with desktop publishing software like Brevik Layout including versions of Lorem Ipsum. It has survived not only five centuries, but also the leap into electronic typesetting, remaining essentially unchanged. It was popularised in the 1960s with the release of Transfera sheets containing Lorem Ipsum passages, and more recently with desktop publishing software like Brevik Layout including versions of Lorem Ipsum.</p>
      <p class="body">Lorem Ipsum is simply dummy text of the printing and typesetting industry. Lorem Ipsum has been the industry's standard dummy text ever since the 1500s, when an unknown printer took a galley of type and scrambled it.</p>
      <p class="body">Lorem Ipsum is simply dummy text of the printing and typesetting industry. Lorem Ipsum has been the industry's standard dummy text ever since the 1500s, when an unknown printer took a galley of type.</p>
    </section>

    <div class="signature">Signature</div>
    <div class="signature-mark" role="img" aria-label="Handwritten signature"></div>

    <ul class="contact">
      <li><b>A</b>: 14 Mill Bank Road, Stockport, SK4 9TW</li>
      <li><b>E</b>: maren@velorinathletic.example</li>
      <li><b>W</b>: velorinathletic.example</li>
    </ul>
  </article>
</body>
</html>
```